A new website for Electrical Contractor Business

We are looking for a unique and new WordPress website design which would include 5 Pages - Home Page, Meet the Team, Our Services, Our Projects and Contact Us page.

The global theme for the website needs to be professional but simple to navigate as we cater for both business and home owner customers.

Our core business service is targeted around lighting from single room decorative to large office so the theme should incorporate this in some way.

The home page should include;
Our business logo, Contact number, Email address, small Image rotation box - Highlighting pervious projectsText box - With welcome message, chirpnet feed news reel/Customer feed back box.

I would also like to see a 2 boxes for the separate customer types we services. Business and Home Owner. each box will have a small image with a small text description with a link to the area of the services page relevant to that customer type.

Meet the team page -This will be introducing potential customers to the team so I would like it to include for each team member. Something like a small image and text area which will introduce an outline of the team members skills and abilities.

Our Services page This page will be outlining the different services on offer to the both customer types business and homeowner. Each service should have an image with text description of the service would good here.

Our projects page-Will include images of pervious projects and work we have completed along with a text area for the project description/ outliner.

Contact Us page - Should include a contact form which should include an option for the customer to quest us to call them back, also a selection box for them to inform us our how they found our details would be good.

Colour - The theme colours can be taken from the logo or feel free to impress with your own imagination.

Remember we are looking for a website that will interest our customers enough to except our services or be drawn further into the website.. So call to action links to other areas of the site/ contact page are welcome

Target Market(s)

Business - Office, warehousing and Large Store - lighting and Power
Home owner lighting and power

Coding

Coded - Design and coding required

Number of Pages Required

5+ page

Font styles to use
Serif
Sans Serif

Colors

Designer to choose colors to be used in the design.

Requirements
Must have
• Logo integrated into the website design - i.e. website colours which allow the logo to blend into the design.
Nice to have
• Custom but professional theme catering to business customers, but also show that we do provide services to home owners too.
Should not have
• Sorry am not interested in one oversized block image on rotation covering half the home page.. Images will be needed but not a single block over sized frame with not text, shape. Please use your imagination when considering this design

```html
<!DOCTYPE html>
<html lang="en">
<head>
<meta charset="utf-8">
<title>Our Services – Brightline Electric</title>
<link href="https://fonts.googleapis.com/css2?family=Roboto+Condensed:wght@400;700&family=Roboto:wght@400;500&display=swap" rel="stylesheet">
<style>
:root{
  --orange:#f26522;
  --navy:#1c2e5c;
  --navy-dark:#223766;
  --heading:#1f3160;
  --text:#3a3a3a;
  --grey:#e6e6e6;
  --white:#ffffff;
}
*{margin:0;padding:0;box-sizing:border-box}
html,body{width:939px;height:1200px;overflow:hidden;background:var(--white)}
body{position:relative;font-family:'Roboto',sans-serif;color:var(--text)}
.hero{position:absolute;left:0;top:0;width:939px;height:270px;
  background:radial-gradient(circle at 30% 40%,#6b4a2e 0%,#3a2a22 40%,#1e1a1c 100%)}
.navbar{position:absolute;left:70px;top:26px;width:800px;height:50px;background:#f7f7f7;display:flex;align-items:center;justify-content:space-between;padding:0 28px 0 16px}
.brand{display:flex;align-items:center;gap:6px;font-family:'Roboto Condensed',sans-serif;font-weight:700;font-size:14px;color:var(--heading);letter-spacing:.5px}
.brand-dot{width:24px;height:24px;border-radius:50%;background:var(--orange)}
.menu{display:flex;gap:26px;font-family:'Roboto Condensed',sans-serif;font-weight:700;font-size:10.5px;color:#111}
.menu .active{color:var(--orange)}
.hero-title{position:absolute;top:146px;width:100%;text-align:center;font-family:'Roboto Condensed',sans-serif;font-weight:700;font-size:39px;color:var(--white);letter-spacing:1px}
.breadcrumb{position:absolute;top:187px;width:100%;text-align:center;font-family:'Roboto Condensed',sans-serif;font-weight:700;font-size:12px;color:var(--white)}
.service{position:absolute;top:351px;width:390px}
.service-photo{width:390px;height:253px}
.service-accent{position:absolute;left:15px;top:237px;width:2px;height:64px;background:var(--orange)}
.service-title{position:absolute;left:35px;top:282px;font-family:'Roboto Condensed',sans-serif;font-weight:700;font-size:21.5px;color:var(--heading);letter-spacing:.5px;white-space:nowrap}
.service-text{position:absolute;left:35px;top:308px;width:336px;font-size:12px;line-height:17.4px;color:var(--text)}
.btn-service{position:absolute;left:35px;top:409px;width:129px;height:30px;background:var(--grey);
  clip-path:polygon(0 0,100% 0,88% 100%,0 100%);font-family:'Roboto Condensed',sans-serif;font-weight:700;font-size:11px;color:#111;line-height:30px;padding-left:24px}
.footer{position:absolute;left:0;top:869px;width:939px;height:331px;background:var(--navy);color:var(--white)}
.footer-brand{position:absolute;left:69px;top:96px;width:160px;text-align:center}
.footer-brand .mark{width:64px;height:64px;border-radius:50%;border:4px solid var(--white);margin:0 auto 10px}
.footer-brand .name{font-family:'Roboto Condensed',sans-serif;font-weight:700;font-size:17px;letter-spacing:1px}
.footer-col{position:absolute;top:83px}
.footer-col h4{font-family:'Roboto Condensed',sans-serif;font-weight:700;font-size:13.5px;letter-spacing:.5px;margin-bottom:9px}
.links li{list-style:none;font-size:11px;height:24.4px}
.newsletter p{font-size:11px;margin-bottom:9px}
.email-field{width:183px;height:29px;background:var(--navy-dark);font-size:9.5px;line-height:29px;padding-left:14px;color:#d8deeb}
.btn-subscribe{margin-top:4px;width:99px;height:29px;background:var(--orange);clip-path:polygon(0 0,100% 0,85% 100%,0 100%);
  font-family:'Roboto Condensed',sans-serif;font-weight:700;font-size:11.5px;line-height:29px;padding-left:15px}
.contact li{list-style:none;font-size:10.5px;height:19px;display:flex;align-items:center;gap:7px}
.contact svg{flex:none}
.socials{display:flex;gap:5px;margin-top:8px;margin-left:5px}
.socials span{width:20px;height:20px;border-radius:50%}
.divider{position:absolute;left:70px;top:288px;width:800px;height:1px;background:#3b4d7a}
.copyright{position:absolute;top:304px;width:100%;text-align:center;font-size:11px}
.to-top{position:absolute;left:881px;top:274px;width:28px;height:28px;border-radius:50%;background:var(--orange);display:flex;align-items:center;justify-content:center}
</style>
</head>
<body>
<header class="hero" role="img" aria-label="Blurred photo of a restaurant interior with warm hanging pendant lights">
  <nav class="navbar">
    <div class="brand"><span class="brand-dot"></span>BRIGHTLINE ELECTRIC</div>
    <div class="menu"><span>HOME</span><span>MEET THE TEAM</span><span class="active">OUR SERVICES</span><span>PROJECTS</span><span>CONTACT US</span></div>
  </nav>
  <h1 class="hero-title">OUR SERVICES</h1>
  <div class="breadcrumb">HOME / OUR SERVICES</div>
</header>

<section class="service" style="left:69px">
  <div class="service-photo" role="img" aria-label="Modern office with glass partitions and a black pendant lamp" style="background:linear-gradient(135deg,#d9d9d6,#8a8279 50%,#4b4540)"></div>
  <div class="service-accent"></div>
  <h2 class="service-title">CUSTOMER TYPE BUSINESS</h2>
  <p class="service-text">Lorem Ipsum is simply dummy text of the printing and typesetting industry. Lorem Ipsum has been the industry's standard dummy text ever since the 1500s, when an unknown printer took a galley of type and scrambled it to make a type specimen book. It has survived not only five centuries,</p>
  <div class="btn-service">GET SERVICE</div>
</section>

<section class="service" style="left:479px">
  <div class="service-photo" role="img" aria-label="Bedroom with blue cushions and a glowing bedside lamp" style="background:linear-gradient(135deg,#b7bcc0,#9aa3aa 45%,#e7e6e2)"></div>
  <div class="service-accent"></div>
  <h2 class="service-title">HOME OWNER</h2>
  <p class="service-text">Lorem Ipsum is simply dummy text of the printing and typesetting industry. Lorem Ipsum has been the industry's standard dummy text ever since the 1500s, when an unknown printer took a galley of type and scrambled it to make a type specimen book. It has survived not only five centuries,</p>
  <div class="btn-service">GET SERVICE</div>
</section>

<footer class="footer">
  <div class="footer-brand"><div class="mark"></div><div class="name">BRIGHTLINE ELECTRIC</div></div>
  <div class="footer-col" style="left:308px">
    <h4>USEFUL LINKS</h4>
    <ul class="links"><li>Home</li><li>Meet the Team</li><li>Our Services</li><li>Projects</li><li>Contact Us</li></ul>
  </div>
  <div class="footer-col newsletter" style="left:498px">
    <h4>NEWSLETTER</h4>
    <p>Subscribe to our newsletter</p>
    <div class="email-field">Email Address</div>
    <div class="btn-subscribe">SUBSCRIBE</div>
  </div>
  <div class="footer-col" style="left:724px">
    <h4>CONTACT US</h4>
    <ul class="contact">
      <li><svg width="9" height="11" viewBox="0 0 9 11"><path d="M4.5 0A4 4 0 0 0 .5 4c0 3 4 7 4 7s4-4 4-7a4 4 0 0 0-4-4zm0 5.5a1.5 1.5 0 1 1 0-3 1.5 1.5 0 0 1 0 3z" fill="#f26522"/></svg>Some goes address here</li>
      <li><svg width="10" height="10" viewBox="0 0 10 10"><path d="M2 0l2 2.5-1.2 1.3a6 6 0 0 0 3.4 3.4L7.5 6 10 8l-1.5 2C4 10 0 6 0 1.5z" fill="#f26522"/></svg>+44 (0140) 227</li>
      <li><svg width="10" height="8" viewBox="0 0 10 8"><rect width="10" height="8" fill="#f26522"/><path d="M0 0l5 4 5-4" stroke="#1c2e5c" fill="none"/></svg>hello@brightline.test</li>
    </ul>
    <div class="socials">
      <span aria-label="social link" style="background:#3b5998"></span>
      <span aria-label="chirpnet" style="background:#1da1f2"></span>
      <span aria-label="social link" style="background:#dd4b39"></span>
    </div>
  </div>
  <div class="divider"></div>
  <div class="copyright">Copyright 2019 | All Right Reserved</div>
  <div class="to-top"><svg width="8" height="5" viewBox="0 0 8 5"><path d="M1 4l3-3 3 3" stroke="#fff" stroke-width="1.4" fill="none"/></svg></div>
</footer>
</body>
</html>
```